Complete Stationary Package for Sea Harvest Trading Company
Silver Lantern Sea Harvest 銀燈海珍
Complete Stationary Package for Sea Harvest Trading Company - Food
Creative Brief
Simple
Malcolm Whitby 马尔
Director of Sales and Distribution
Silver Lantern Sea Harvest, Level 11, KL Plaza 5, Jalan Kenari Raya, Bangsar, 59100 Kuala Lumpur, Malaysia
mwhitby@slseaharvest-example.com
www.slseaharvest-example.com
We need a full stationary package design - business cards, letterhead, envelopes, folders, invoice, email signature and any other standard stationary items you may decide to include in your concepts. I need the text below written in smaller print somewhere on the card either on the front or the back " Silver Lantern Sea Harvest is a registered trademark of Corvale Holdings Sdn Bhd 8827165K". I like the same cream colour that is used in the packaging that I have uploaded. I do not want the card to have a white background colour. I would like red and/or gold to feature also.
I would like a suitable design for the back of the card with the company name and logo.

```html
<!DOCTYPE html>
<html lang="en">
<head>
<meta charset="utf-8">
<title>Silver Lantern Sea Harvest – Stationery Package</title>
<link href="https://fonts.googleapis.com/css2?family=Lato:wght@400;700&family=Noto+Serif+TC:wght@600&display=swap" rel="stylesheet">
<style>
:root{
  --bg:#47423d;
  --paper:#ffffff;
  --cream:#f6ecd6;
  --gold-dark:#b8862b;
  --gold:#d9ab4a;
  --gold-light:#f3d88c;
  --red:#d42a2a;
  --ink:#4a4a4a;
  --muted:#8a8a8a;
}
*{box-sizing:border-box;margin:0;padding:0}
html,body{width:1200px;height:942px;overflow:hidden}
body{background:var(--bg);font-family:"Lato",sans-serif;color:var(--ink);position:relative}
.item{position:absolute;overflow:hidden;background:var(--paper);box-shadow:0 3px 8px rgba(0,0,0,.35)}
.gold-bg{background:linear-gradient(135deg,var(--gold-dark),var(--gold-light) 45%,var(--gold) 70%,var(--gold-dark))}
.cream-bg{background:var(--cream)}
.wave{position:absolute;left:0;bottom:0;width:100%;display:block}
.brand{display:flex;flex-direction:column;align-items:center;gap:2px;font-family:"Noto Serif TC",serif;font-weight:600;color:var(--gold-dark);text-align:center;line-height:1.1}
.brand .dot{width:16px;height:16px;border-radius:50%;background:var(--gold)}
.brand .zh{font-size:9px;letter-spacing:1px;white-space:nowrap}
.brand .en{font-size:5px;letter-spacing:.3px}
.brand.on-gold{color:#fff}
.brand.on-gold .dot{background:#fff}
.brand.lg .dot{width:28px;height:28px}
.brand.lg .zh{font-size:15px}
.brand.lg .en{font-size:7px}
.brand.narrow{width:52px}
.brand.narrow .en{font-size:4.5px;line-height:1.2}
.small{font-size:4px;line-height:1.5;color:var(--ink)}
.tiny{font-size:3.5px;line-height:1.5;color:var(--muted)}
.abs{position:absolute}
.body-text p{margin-bottom:3px}
.footer-line{position:absolute;left:0;right:0;bottom:4px;text-align:center;font-size:3.5px;color:var(--gold-dark)}
.invoice-title{font-size:9px;font-weight:700;color:var(--red);letter-spacing:1px}
.inv-table{position:absolute;left:14px;right:14px;top:118px;border-collapse:collapse;font-size:3.5px}
.inv-table th{background:var(--cream);color:var(--gold-dark);text-align:left;padding:2px;border:.5px solid var(--gold-light)}
.inv-table td{height:8px;border:.5px solid #eee;padding:2px}
.thanks{font-size:18px;color:var(--red);font-weight:400}
.notepad-label{font-size:9px;letter-spacing:2px;color:var(--ink)}
.name{font-size:6px;font-weight:700;color:var(--ink);white-space:nowrap}
.role{font-size:3.8px;color:var(--red);white-space:nowrap}
.flap{position:absolute;left:0;top:0;width:100%;height:100%}
</style>
</head>
<body>

<svg width="0" height="0" style="position:absolute" aria-hidden="true">
  <defs>
    <linearGradient id="goldfade" x1="0" x2="1" y1="0" y2="0">
      <stop offset="0" stop-color="#b8862b"/>
      <stop offset=".5" stop-color="#f3d88c"/>
      <stop offset="1" stop-color="#c99733"/>
    </linearGradient>
  </defs>
</svg>

<!-- Business cards -->
<section class="item cream-bg" style="left:46px;top:51px;width:138px;height:77px">
  <div class="brand narrow abs" style="left:8px;top:14px"><span class="dot"></span><span class="zh">銀燈海珍</span><span class="en">Silver Lantern Sea Harvest</span></div>
  <div class="abs" style="left:68px;top:16px;width:64px">
    <div class="name">Malcolm Whitby 马尔</div>
    <div class="role">Director of Sales and Distribution</div>
  </div>
  <div class="abs tiny" style="left:68px;top:36px;width:64px">Level 11, KL Plaza 5, Jalan Kenari Raya, Bangsar, 59100 Kuala Lumpur<br>mwhitby@slseaharvest-example.com<br>www.slseaharvest-example.com</div>
</section>
<section class="item cream-bg" style="left:46px;top:140px;width:138px;height:77px">
  <div class="brand abs" style="left:10px;top:10px"><span class="dot"></span><span class="zh">銀燈海珍</span><span class="en">Silver Lantern Sea Harvest</span></div>
  <div class="abs tiny" style="left:10px;bottom:6px;width:120px">Silver Lantern Sea Harvest is a registered trademark of Corvale Holdings Sdn Bhd 8827165K</div>
</section>
<section class="item gold-bg" style="left:46px;top:225px;width:138px;height:77px">
  <div class="brand on-gold abs" style="left:0;right:0;top:18px"><span class="dot"></span><span class="zh">銀燈海珍</span><span class="en">Silver Lantern Sea Harvest</span></div>
</section>

<!-- Letterhead 1 -->
<article class="item" style="left:209px;top:51px;width:199px;height:268px">
  <div class="brand abs" style="left:14px;top:12px"><span class="dot"></span><span class="zh">銀燈海珍</span><span class="en">Silver Lantern Sea Harvest</span></div>
  <div class="abs tiny" style="right:12px;top:14px;text-align:right">Level 11, KL Plaza 5<br>Jalan Kenari Raya, Bangsar<br>59100 Kuala Lumpur, Malaysia</div>
  <div class="abs small body-text" style="left:14px;right:14px;top:62px">
    <p>Dear Partner,</p>
    <p>Thank you for your continued trust in our seafood products. We are pleased to share our new season catalogue and pricing with you.</p>
    <p>Our team will contact you shortly to arrange delivery schedules and answer any questions you may have.</p>
    <p>Kind regards,<br>Malcolm Whitby</p>
  </div>
  <svg class="wave" viewBox="0 0 200 40" preserveAspectRatio="none" height="36" aria-hidden="true"><path d="M0 20 C60 4 130 38 200 12 L200 40 L0 40Z" fill="url(#goldfade)"/><path d="M0 16 C60 0 130 34 200 8" stroke="var(--red)" stroke-width="2.5" fill="none"/><path d="M0 30 C70 20 140 44 200 26 L200 40 L0 40Z" fill="#fff"/></svg>
  <div class="footer-line">www.slseaharvest-example.com</div>
</article>

<!-- Letterhead 2 -->
<article class="item" style="left:424px;top:51px;width:199px;height:268px">
  <div class="brand abs" style="left:0;right:0;top:12px"><span class="dot"></span><span class="zh">銀燈海珍</span><span class="en">Silver Lantern Sea Harvest</span></div>
  <div class="abs small body-text" style="left:14px;right:14px;top:62px">
    <p>Dear Customer,</p>
    <p>We are delighted to confirm your order and appreciate your support. Our products are carefully selected and packed fresh.</p>
    <p>Please find the order details attached for your records.</p>
    <p>Sincerely,<br>Malcolm Whitby</p>
  </div>
  <svg class="wave" viewBox="0 0 200 40" preserveAspectRatio="none" height="36" aria-hidden="true"><path d="M0 20 C60 4 130 38 200 12 L200 40 L0 40Z" fill="url(#goldfade)"/><path d="M0 16 C60 0 130 34 200 8" stroke="var(--red)" stroke-width="2.5" fill="none"/><path d="M0 30 C70 20 140 44 200 26 L200 40 L0 40Z" fill="#fff"/></svg>
  <div class="footer-line">mwhitby@slseaharvest-example.com</div>
</article>

<!-- Invoice -->
<article class="item" style="left:648px;top:51px;width:200px;height:268px">
  <div class="brand abs" style="left:14px;top:12px"><span class="dot"></span><span class="zh">銀燈海珍</span><span class="en">Silver Lantern Sea Harvest</span></div>
  <div class="abs invoice-title" style="right:14px;top:16px">INVOICE</div>
  <div class="abs tiny" style="left:14px;top:70px">Bill to: Customer Name<br>Address Line<br>Date: 00/00/0000</div>
  <table class="inv-table">
    <tr><th>Item</th><th>Qty</th><th>Price</th><th>Total</th></tr>
    <tr><td></td><td></td><td></td><td></td></tr>
    <tr><td></td><td></td><td></td><td></td></tr>
    <tr><td></td><td></td><td></td><td></td></tr>
    <tr><td></td><td></td><td></td><td></td></tr>
  </table>
  <svg class="wave" viewBox="0 0 200 40" preserveAspectRatio="none" height="36" aria-hidden="true"><path d="M0 20 C60 4 130 38 200 12 L200 40 L0 40Z" fill="url(#goldfade)"/><path d="M0 16 C60 0 130 34 200 8" stroke="var(--red)" stroke-width="2.5" fill="none"/><path d="M0 30 C70 20 140 44 200 26 L200 40 L0 40Z" fill="#fff"/></svg>
  <div class="footer-line">www.slseaharvest-example.com</div>
</article>

<!-- Compliment slips -->
<section class="item" style="left:870px;top:46px;width:138px;height:82px">
  <div class="brand abs" style="left:0;right:0;top:8px"><span class="dot"></span><span class="zh">銀燈海珍</span><span class="en">Silver Lantern Sea Harvest</span></div>
  <svg class="wave" viewBox="0 0 200 40" preserveAspectRatio="none" height="14" aria-hidden="true"><path d="M0 20 C60 4 130 38 200 12 L200 40 L0 40Z" fill="url(#goldfade)"/><path d="M0 16 C60 0 130 34 200 8" stroke="var(--red)" stroke-width="3" fill="none"/></svg>
</section>
<section class="item" style="left:870px;top:143px;width:138px;height:74px">
  <div class="brand abs" style="left:8px;top:8px"><span class="dot"></span><span class="zh">銀燈海珍</span></div>
  <div class="abs tiny" style="left:8px;top:44px">With compliments</div>
  <svg class="wave" viewBox="0 0 200 40" preserveAspectRatio="none" height="12" aria-hidden="true"><path d="M0 20 C60 4 130 38 200 12 L200 40 L0 40Z" fill="url(#goldfade)"/><path d="M0 16 C60 0 130 34 200 8" stroke="var(--red)" stroke-width="3" fill="none"/></svg>
</section>

<!-- DL envelopes -->
<section class="item gold-bg" style="left:876px;top:250px;width:171px;height:30px">
  <div class="abs" style="left:8px;top:8px;font-family:'Noto Serif TC',serif;font-weight:600;font-size:9px;color:#fff">銀燈海珍</div>
</section>
<section class="item" style="left:876px;top:285px;width:171px;height:42px">
  <svg class="flap" viewBox="0 0 171 42" preserveAspectRatio="none" aria-hidden="true"><path d="M0 0 L85 24 L171 0" stroke="#ddd" stroke-width="1" fill="none"/></svg>
</section>

<!-- Presentation folder -->
<section class="item" style="left:46px;top:378px;width:401px;height:265px">
  <div class="gold-bg abs" style="left:0;top:0;width:200px;height:100%"></div>
  <div class="brand on-gold lg abs" style="left:0;width:200px;top:70px"><span class="dot"></span><span class="zh">銀燈海珍</span><span class="en">Silver Lantern Sea Harvest</span></div>
  <div class="abs" style="left:14px;bottom:14px;font-size:4px;line-height:1.5;color:#fff;width:170px">Level 11, KL Plaza 5, Jalan Kenari Raya, Bangsar, 59100 Kuala Lumpur, Malaysia<br>www.slseaharvest-example.com</div>
  <svg class="abs" style="left:200px;bottom:0" width="201" height="46" viewBox="0 0 200 40" preserveAspectRatio="none" aria-hidden="true"><path d="M0 20 C60 4 130 38 200 12 L200 40 L0 40Z" fill="url(#goldfade)"/><path d="M0 16 C60 0 130 34 200 8" stroke="var(--red)" stroke-width="2.5" fill="none"/><path d="M0 30 C70 20 140 44 200 26 L200 40 L0 40Z" fill="#fff"/></svg>
</section>

<!-- Large envelope -->
<section class="item" style="left:46px;top:659px;width:401px;height:235px">
  <div class="brand abs" style="left:16px;top:16px"><span class="dot"></span><span class="zh">銀燈海珍</span><span class="en">Silver Lantern Sea Harvest</span></div>
  <div class="gold-bg abs" style="right:0;top:0;width:140px;height:100%"></div>
</section>

<!-- Business card spread -->
<section class="item" style="left:510px;top:345px;width:120px;height:70px">
  <div class="brand abs" style="left:6px;top:8px"><span class="dot"></span><span class="zh">銀燈海珍</span></div>
  <div class="abs" style="left:6px;top:40px"><div class="name">Malcolm Whitby</div><div class="tiny">Level 11, KL Plaza 5, Bangsar</div></div>
</section>
<section class="item cream-bg" style="left:640px;top:345px;width:126px;height:70px">
  <div class="brand abs" style="left:6px;top:6px"><span class="dot"></span></div>
  <div class="abs" style="left:30px;top:8px"><div class="name">Malcolm Whitby</div><div class="role">Director of Sales and Distribution</div></div>
  <div class="abs tiny" style="left:30px;top:30px">mwhitby@slseaharvest-example.com<br>www.slseaharvest-example.com</div>
</section>

<!-- Thank you card -->
<section class="item gold-bg" style="left:659px;top:455px;width:135px;height:30px"></section>
<section class="item" style="left:659px;top:490px;width:235px;height:174px">
  <div class="brand abs" style="left:0;right:0;top:14px"><span class="dot"></span><span class="zh">銀燈海珍</span><span class="en">Silver Lantern Sea Harvest</span></div>
  <div class="abs thanks" style="left:20px;top:98px">Thank you !</div>
  <svg class="wave" viewBox="0 0 200 40" preserveAspectRatio="none" height="24" aria-hidden="true"><path d="M0 20 C60 4 130 38 200 12 L200 40 L0 40Z" fill="url(#goldfade)"/><path d="M0 16 C60 0 130 34 200 8" stroke="var(--red)" stroke-width="2.5" fill="none"/></svg>
</section>

<!-- Note pad -->
<section class="item" style="left:919px;top:460px;width:148px;height:224px">
  <div class="brand abs" style="left:0;right:0;top:16px"><span class="dot"></span><span class="zh">銀燈海珍</span><span class="en">Silver Lantern Sea Harvest</span></div>
  <svg class="abs" style="left:0;top:70px" width="148" height="26" viewBox="0 0 200 40" preserveAspectRatio="none" aria-hidden="true"><path d="M0 20 C60 4 130 38 200 12 L200 40 L0 40Z" fill="url(#goldfade)"/><path d="M0 16 C60 0 130 34 200 8" stroke="var(--red)" stroke-width="3" fill="none"/><path d="M0 30 C70 20 140 44 200 26 L200 40 L0 40Z" fill="#fff"/></svg>
  <div class="abs notepad-label" style="left:0;right:0;bottom:28px;text-align:center">NOTE PAD</div>
</section>

<!-- Postcard back -->
<section class="item" style="left:1085px;top:410px;width:80px;height:110px">
  <div class="brand abs" style="left:6px;top:8px"><span class="dot"></span></div>
  <svg class="abs" style="left:42px;top:40px" width="32" height="40" aria-hidden="true"><line x1="0" y1="6" x2="32" y2="6" stroke="#ccc" stroke-width=".6"/><line x1="0" y1="18" x2="32" y2="18" stroke="#ccc" stroke-width=".6"/><line x1="0" y1="30" x2="32" y2="30" stroke="#ccc" stroke-width=".6"/></svg>
  <svg class="wave" viewBox="0 0 200 40" preserveAspectRatio="none" height="10" aria-hidden="true"><path d="M0 20 C60 4 130 38 200 12 L200 40 L0 40Z" fill="url(#goldfade)"/></svg>
</section>

<!-- CD and sleeve -->
<section class="item" style="left:562px;top:669px;width:130px;height:130px">
  <div class="brand narrow abs" style="left:14px;top:16px"><span class="dot"></span><span class="zh">銀燈海珍</span><span class="en">Silver Lantern Sea Harvest</span></div>
  <div class="abs tiny" style="left:8px;bottom:10px;width:72px">Level 11, KL Plaza 5, Jalan Kenari Raya, Bangsar</div>
</section>
<section class="gold-bg abs" style="left:620px;top:760px;width:130px;height:129px;box-shadow:0 3px 8px rgba(0,0,0,.35)"></section>
<svg class="abs" style="left:650px;top:669px" width="140" height="140" viewBox="0 0 140 140" aria-hidden="true">
  <circle cx="70" cy="70" r="68" fill="#fff" stroke="#e5e5e5"/>
  <path d="M2 82 C40 70 100 100 138 78" stroke="var(--red)" stroke-width="3" fill="none"/>
  <circle cx="70" cy="70" r="14" fill="#eee"/>
  <circle cx="70" cy="70" r="7" fill="var(--bg)"/>
</svg>
<div class="brand abs" style="left:690px;top:688px"><span class="zh">銀燈海珍</span></div>

</body>
</html>
```